Sales brochure to promote delivery services

we need new revamped marketing brochure
We are a 3rd Party Logistics company specializing in home delivery and assembly for the home furnishings market. our company provides delivery services, we provide trained delivery teams, we also provide online order tracking, we provide routing and dispatching, expert handling of merchandise, white glove service. the brochure is going to be used for sales dept to leave/mail to potential customers. brochure is intended to give information about our services and attract business.

Target Market(s)

home furniture retailers, furniture and appliance retailers, retailers that require delivery services

Industry/Entity Type

Delivery Service

Requirements
Must have
• color scheme coordinates with company logo
• phone number 415.273-6150 and website address www.bravecrest-3pl.com
Nice to have
• tri-fold design preferred
• include artwork and/or pictures related to our services examples would be dining room, living room, bedroom furniture, kitchen appliances, laundry, white box delivery truck, happy customers

```html
<!DOCTYPE html>
<html lang="en">
<head>
<meta charset="utf-8">
<title>Bravecrest Logistics Tri-fold Brochure</title>
<link rel="stylesheet" href="https://fonts.googleapis.com/css2?family=Montserrat:wght@300;400;500;600;700;800&family=Open+Sans:wght@400;600&display=swap">
<style>
:root{
  --lime:#c3d52a;
  --olive:#a9ad18;
  --olive-dark:#8f9613;
  --navy:#0d2536;
  --navy-mid:#173f57;
  --purple:#3d3a78;
  --ink:#1b1b28;
  --paper:#ffffff;
  --bg:#e4e5e7;
}
*{margin:0;padding:0;box-sizing:border-box}
html,body{width:1200px;height:947px;overflow:hidden;background:var(--bg)}
body{font-family:"Montserrat",sans-serif;position:relative}
.brochure{position:absolute;left:60px;top:54px;width:1080px;height:838px;display:flex;box-shadow:0 6px 18px rgba(0,0,0,.18)}
.panel{position:relative;width:360px;height:838px;overflow:hidden}
.panel::before,.panel::after{content:"";position:absolute;left:0;right:0;height:9px;z-index:5;background:linear-gradient(90deg,var(--olive),var(--lime),var(--olive))}
.panel::before{top:0}
.panel::after{bottom:0}
.panel--inside-flap{background:var(--paper)}
.panel--back{background:linear-gradient(180deg,var(--navy-mid) 0%,#123347 40%,var(--navy) 100%)}
.panel--back::before{background:linear-gradient(90deg,#123347,#1b4660)}
.panel--cover{background:var(--paper)}
.panel--cover::before{background:linear-gradient(90deg,#0f2b3d,#1c4a63)}

.intro{position:absolute;top:26px;left:34px;right:34px;text-align:center;font-family:"Montserrat",sans-serif;font-weight:400;font-size:16px;line-height:22px;color:var(--ink)}
.benefit{position:absolute;left:30px;right:36px;border:1px dotted var(--olive);border-radius:4px;color:var(--purple);font-weight:600;font-size:16.5px;text-align:center;line-height:18px;padding:4px 6px}
.benefit .bullet{position:absolute;left:-6px;top:50%;transform:translateY(-50%);width:13px;height:13px}
.pill{position:absolute;top:270px;left:70px;width:215px;height:33px;border-radius:5px;background:var(--purple);color:#fff;font-size:19px;line-height:33px;text-align:center;box-shadow:0 3px 5px rgba(0,0,0,.25)}
.pill strong{color:var(--lime);font-weight:700}
.flap-art{position:absolute;left:0;top:432px;width:360px;height:406px}
.bottom-line{position:absolute;left:0;right:0;top:714px;text-align:center}
.bottom-line .lead{color:#fff;font-size:19px;font-weight:400}
.bottom-line .big{color:var(--olive);font-size:38px;font-weight:800;line-height:36px;margin-top:5px}

.back-photo{position:absolute;left:0;top:0;width:360px;height:160px}
.back-copy{position:absolute;left:0;right:0;text-align:center}
.rule{width:40px;height:2px;background:var(--olive);margin:0 auto}
.kicker{color:#e9eef2;font-size:21px;font-weight:400}
.lime-caps{color:var(--lime);font-size:20px;font-weight:700;line-height:26px}
.white-caps{color:#fff;font-size:20px;font-weight:600;line-height:27px}
.lime-line{color:var(--lime);font-size:18.5px;font-weight:400}
.win-light{color:var(--lime);font-size:37px;font-weight:300;line-height:40px}
.win-bold{color:#fff;font-size:57px;font-weight:800;line-height:58px;letter-spacing:-1px}
.team-circle{position:absolute;left:69px;top:484px;width:200px;height:200px}
.company{position:absolute;top:699px;left:0;right:0;text-align:center;color:var(--olive);font-size:16px;font-weight:700}
.contact{position:absolute;top:726px;left:0;right:0;text-align:center;font-family:"Open Sans",sans-serif;color:#fff;font-size:12.5px;line-height:19px}
.contact svg{width:10px;height:10px;vertical-align:-1px;margin-right:4px}

.brand{position:absolute;top:76px;left:0;right:0;text-align:center;font-size:22px;font-weight:600;color:var(--purple)}
.cover-art{position:absolute;left:0;top:168px;width:360px;height:512px}
.headline{position:absolute;top:620px;left:0;right:0;text-align:center;line-height:1}
.headline .h1{font-size:38px;font-weight:400;color:var(--ink)}
.headline .h2{font-size:44px;font-weight:800;color:var(--olive);margin-top:2px;letter-spacing:-.5px}
.headline .h3{display:inline-block;background:var(--purple);color:#fff;font-size:37px;font-weight:700;letter-spacing:7px;padding:2px 2px 1px 9px;margin-top:2px}
.cover-phone{position:absolute;top:772px;left:0;right:0;text-align:center;color:var(--olive);font-size:24px;font-weight:700}
.cover-phone svg{width:19px;height:19px;vertical-align:-2px;margin-right:4px}
.cover-web{position:absolute;top:802px;left:0;right:0;text-align:center;font-family:"Open Sans",sans-serif;color:var(--ink);font-size:15.5px}
</style>
</head>
<body>
<main class="brochure">

  <section class="panel panel--inside-flap">
    <p class="intro">Our team of improvement professionals will help you with the areas that mean the most to your business:</p>

    <div class="benefit" style="top:138px;left:52px;right:60px"><svg class="bullet" viewBox="0 0 14 14"><circle cx="7" cy="7" r="7" fill="#a9ad18"/><path d="M5.5 4l3 3-3 3" stroke="#fff" stroke-width="1.8" fill="none"/></svg>Higher on-time delivery</div>
    <div class="benefit" style="top:172px"><svg class="bullet" viewBox="0 0 14 14"><circle cx="7" cy="7" r="7" fill="#a9ad18"/><path d="M5.5 4l3 3-3 3" stroke="#fff" stroke-width="1.8" fill="none"/></svg>Lower Exchanges &amp; Damages</div>
    <div class="benefit" style="top:206px"><svg class="bullet" viewBox="0 0 14 14"><circle cx="7" cy="7" r="7" fill="#a9ad18"/><path d="M5.5 4l3 3-3 3" stroke="#fff" stroke-width="1.8" fill="none"/></svg>Greater Customer Satisfaction</div>

    <div class="pill">At <strong>BRAVECREST</strong> We:</div>

    <div class="benefit" style="top:327px;font-size:16px;line-height:17px"><svg class="bullet" viewBox="0 0 14 14"><circle cx="7" cy="7" r="7" fill="#a9ad18"/><path d="M5.5 4l3 3-3 3" stroke="#fff" stroke-width="1.8" fill="none"/></svg>Practice a simple no-nonsense approach to problem solving</div>
    <div class="benefit" style="top:378px;font-size:16px;line-height:18px"><svg class="bullet" viewBox="0 0 14 14"><circle cx="7" cy="7" r="7" fill="#a9ad18"/><path d="M5.5 4l3 3-3 3" stroke="#fff" stroke-width="1.8" fill="none"/></svg>Are efficient, resourceful and thorough</div>

    <svg class="flap-art" viewBox="0 0 360 406" preserveAspectRatio="none">
      <defs>
        <linearGradient id="handshakeTone" x1="0" y1="0" x2="1" y2="1">
          <stop offset="0" stop-color="#ffffff"/>
          <stop offset=".5" stop-color="#c9c9c9"/>
          <stop offset="1" stop-color="#8d8d8d"/>
        </linearGradient>
        <linearGradient id="flapGreen" x1="0" y1="0" x2="1" y2="0">
          <stop offset="0" stop-color="#8f9613"/>
          <stop offset=".5" stop-color="#c3d52a"/>
          <stop offset="1" stop-color="#a9ad18"/>
        </linearGradient>
      </defs>
      <rect x="0" y="0" width="360" height="260" fill="url(#handshakeTone)" role="img" aria-label="Black and white photo of a business handshake"/>
      <path d="M0 75 C60 185 200 245 360 238 L360 406 L0 406 Z" fill="url(#flapGreen)"/>
      <path d="M0 195 C90 250 230 275 360 266 L360 406 L0 406 Z" fill="#0d2536"/>
      <path d="M0 195 C90 250 230 275 360 266" stroke="#d8e36a" stroke-width="2" fill="none" opacity=".6"/>
    </svg>

    <div class="bottom-line">
      <div class="lead">WE'RE HERE TO HELP YOU</div>
      <div class="big">IMPROVE YOUR<br>BOTTOM LINE</div>
    </div>
  </section>

  <section class="panel panel--back">
    <svg class="back-photo" viewBox="0 0 360 160" preserveAspectRatio="none" role="img" aria-label="Photo of a smiling customer service agent wearing a headset, tinted blue">
      <defs>
        <linearGradient id="agentTint" x1="0" y1="0" x2="0" y2="1">
          <stop offset="0" stop-color="#2d6d88"/>
          <stop offset=".6" stop-color="#1f5570"/>
          <stop offset="1" stop-color="#173f57" stop-opacity="0"/>
        </linearGradient>
      </defs>
      <rect width="360" height="160" fill="url(#agentTint)"/>
    </svg>

    <div class="back-copy" style="top:154px">
      <div class="kicker">Bravecrest is</div>
      <div class="lime-caps">WHAT HAPPENS WHEN<br>YOU GET MOVING...</div>
      <div class="rule" style="margin-top:14px"></div>
    </div>
    <div class="back-copy" style="top:258px">
      <div class="lime-line">Building Bravecrest is</div>
      <div class="white-caps" style="margin-top:3px">FOLLOWING ONE<br>SUCCESS IMMEDIATELY<br>WITH ANOTHER.</div>
      <div class="rule" style="margin-top:14px"></div>
    </div>
    <div class="back-copy" style="top:392px">
      <div class="win-light">When You Win,</div>
      <div class="win-bold">WE WIN!</div>
    </div>

    <svg class="team-circle" viewBox="0 0 200 200">
      <defs>
        <radialGradient id="ringGlow" cx=".5" cy=".5" r=".5">
          <stop offset=".8" stop-color="#1d4a62"/>
          <stop offset="1" stop-color="#0d2536"/>
        </radialGradient>
        <linearGradient id="teamTone" x1="0" y1="0" x2="1" y2="1">
          <stop offset="0" stop-color="#dbe9f2"/>
          <stop offset="1" stop-color="#93b6cb"/>
        </linearGradient>
      </defs>
      <circle cx="100" cy="100" r="99" fill="url(#ringGlow)"/>
      <circle cx="100" cy="100" r="90" fill="#e8eef2"/>
      <circle cx="100" cy="100" r="84" fill="url(#teamTone)" role="img" aria-label="Photo of a team stacking their hands together"/>
    </svg>

    <div class="company">BRAVECREST LOGISTICS, INC.</div>
    <div class="contact">
      <div><svg viewBox="0 0 10 10"><circle cx="5" cy="5" r="5" fill="#fff"/><circle cx="5" cy="4.2" r="1.6" fill="#0d2536"/></svg>18 Harborview Drive Suite 400<br>Oakridge CA 94107</div>
      <div><svg viewBox="0 0 10 10"><circle cx="5" cy="5" r="5" fill="#fff"/><path d="M3.4 2.6l1 1.2-.5.7c.4.8 1 1.4 1.7 1.7l.7-.5 1.2 1-.6.9c-2 0-3.9-1.9-4-4z" fill="#0d2536"/></svg>415.273-6150</div>
      <div><svg viewBox="0 0 10 10"><circle cx="5" cy="5" r="5" fill="#fff"/><rect x="2.6" y="3.3" width="4.8" height="3.4" fill="#0d2536"/><path d="M2.6 3.3l2.4 2 2.4-2" stroke="#fff" stroke-width=".6" fill="none"/></svg>inquiries@bravecrest-3pl.com</div>
      <div><svg viewBox="0 0 10 10"><circle cx="5" cy="5" r="5" fill="#fff"/><circle cx="5" cy="5" r="2.6" fill="none" stroke="#0d2536" stroke-width=".8"/><path d="M2.4 5h5.2M5 2.4v5.2" stroke="#0d2536" stroke-width=".6"/></svg>www.bravecrest-3pl.com</div>
    </div>
  </section>

  <section class="panel panel--cover">
    <div class="brand">Bravecrest Logistics</div>

    <svg class="cover-art" viewBox="0 0 360 512" preserveAspectRatio="none">
      <defs>
        <linearGradient id="crewTone" x1="0" y1="0" x2="1" y2="1">
          <stop offset="0" stop-color="#f2f2f4"/>
          <stop offset=".45" stop-color="#b9bfd3"/>
          <stop offset="1" stop-color="#2a2f63"/>
        </linearGradient>
        <linearGradient id="coverGreen" x1="0" y1="0" x2="1" y2="0">
          <stop offset="0" stop-color="#a9ad18"/>
          <stop offset=".6" stop-color="#c3d52a"/>
          <stop offset="1" stop-color="#8f9613"/>
        </linearGradient>
      </defs>
      <rect x="0" y="40" width="360" height="380" fill="url(#crewTone)" role="img" aria-label="Photo of a smiling dispatcher with a headset and a delivery worker in navy caps"/>
      <path d="M0 365 C120 335 280 345 360 390 L360 512 L0 512 Z" fill="url(#coverGreen)"/>
      <path d="M0 390 C120 360 290 380 360 470 L360 512 L0 512 Z" fill="#ffffff"/>
    </svg>

    <div class="headline">
      <div class="h1">HOME DELIVERY</div>
      <div class="h2">&amp; ASSEMBLY</div>
      <div class="h3">SOLUTIONS</div>
    </div>
    <div class="cover-phone"><svg viewBox="0 0 20 20"><circle cx="10" cy="10" r="10" fill="#3d3a78"/><path d="M6.6 5.2l2 2.4-1 1.4c.8 1.6 2 2.8 3.4 3.4l1.4-1 2.4 2-1.2 1.8c-4 0-7.8-3.8-8-8z" fill="#fff"/></svg>415.273-6150</div>
    <div class="cover-web">www.bravecrest-3pl.com</div>
  </section>

</main>
</body>
</html>
```